Business Cards for a law firm

Business cards for our law firm. Use our silhoette logo and OAK HARBOR - check our website (www.oakharbor-legal.com)

Contact Information for Business Card

our silhouette logo, OAK HARBOR, 800-555-0147, Dorian Kestrup, dorian@oakharbor-legal.com

Requirements
Must have
• our silhouette logo, OAK HARBOR, 800-555-0147, Dorian Kestrup, dorian@oakharbor-legal.com

```html
<!DOCTYPE html>
<html lang="en">
<head>
<meta charset="utf-8">
<title>Oak Harbor – Business Cards</title>
<link rel="stylesheet" href="https://fonts.googleapis.com/css2?family=Arimo:wght@400;500&display=swap">
<style>
  :root {
    --backdrop: #6e6e6e;
    --card-white: #ffffff;
    --navy: #25305a;
    --amber: #f5a21c;
    --text-light: #ffffff;
  }
  * { margin: 0; padding: 0; box-sizing: border-box; }
  html, body {
    width: 1200px;
    height: 1000px;
    overflow: hidden;
    background: var(--backdrop);
    font-family: "Arimo", Arial, sans-serif;
  }
  .canvas {
    position: relative;
    width: 1200px;
    height: 1000px;
  }
  .card {
    position: absolute;
    width: 700px;
    height: 410px;
  }
  .card--back {
    left: 420px;
    top: 480px;
    background: var(--navy);
  }
  .card--front {
    left: 110px;
    top: 140px;
    background: var(--card-white);
    display: flex;
    align-items: center;
    justify-content: center;
    gap: 18px;
    z-index: 2;
  }
  .brand-mark {
    width: 22px;
    height: 22px;
    background: var(--navy);
  }
  .brand-name {
    color: var(--navy);
    font-weight: 500;
    font-size: 42px;
    letter-spacing: 3px;
  }
  .contact {
    position: absolute;
    left: 200px;
    top: 190px;
    color: var(--text-light);
  }
  .contact__name {
    font-size: 20px;
    font-weight: 400;
  }
  .contact__phone {
    color: var(--amber);
    font-size: 50px;
    font-weight: 500;
    line-height: 1.05;
    margin-top: 2px;
  }
  .contact__email {
    font-size: 20px;
    font-weight: 400;
    margin-top: 6px;
  }
</style>
</head>
<body>
  <main class="canvas">
    <section class="card card--front" aria-label="Business card front">
      <span class="brand-mark" aria-hidden="true"></span>
      <span class="brand-name">OAK HARBOR</span>
    </section>

    <section class="card card--back" aria-label="Business card back">
      <div class="contact">
        <p class="contact__name">Dorian Kestrup</p>
        <p class="contact__phone">800-555-0147</p>
        <p class="contact__email">dorian@oakharbor-legal.com</p>
      </div>
    </section>
  </main>
</body>
</html>
```